A Flyer for a clinic/hospital waiting room to warn about patients that they must not abuse our staff

we need a flyer (text attached) with a background of a female nurse or medical doctor photo. I like the example photo where there are four headless satff lined up - something like this, indicating that we are a team and will not tolerate abuse
A4
the text will be over the photo.

Target Market(s)

patients who come to our clinic

Industry/Entity Type

medicine - urology

Colors
0054AA
0677BA
7BADD7
CADEEF
E8F1F8
0094D4
00A9DD
6FCCEA
C7EBF8
E9F6FB

Requirements
Must have
• a photo taking up the whole A4, and text over this. The photos I haev sent are just examples - I will need yo to source a photo
Nice to have
• Horizontal A4 and vertical A4 options. Please add our logo in small , in the bottom right corner

```html
<!DOCTYPE html>
<html lang="en">
<head>
<meta charset="utf-8">
<title>Zero-Tolerance Flyer</title>
<link href="https://fonts.googleapis.com/css2?family=Montserrat:wght@400;500;600;700;800;900&display=swap" rel="stylesheet">
<style>
  :root {
    --navy: #0054AA;
    --blue: #0677BA;
    --sky: #7BADD7;
    --mist: #CADEEF;
    --ice: #E8F1F8;
    --cyan: #0094D4;
    --aqua: #00A9DD;
    --pale-aqua: #C7EBF8;
    --ink: #111418;
    --band: #1d2024;
    --paper: #ffffff;
    --backdrop: #f1f2f3;
    --muted: #4a4f55;
  }
  * { box-sizing: border-box; margin: 0; padding: 0; }
  html, body { width: 1200px; height: 2640px; overflow: hidden; }
  body {
    background: var(--backdrop);
    font-family: "Montserrat", Arial, sans-serif;
    position: relative;
  }
  .flyer {
    position: absolute;
    left: 100px; top: 613px;
    width: 1000px; height: 1414px;
    background: var(--paper);
    overflow: hidden;
    box-shadow: 0 2px 10px rgba(0,0,0,0.08);
  }
  .network-backdrop {
    position: absolute; left: 0; top: 0; width: 1000px; height: 480px;
    background:
      radial-gradient(circle at 8% 10%, var(--pale-aqua) 0, rgba(199,235,248,0) 32%),
      radial-gradient(circle at 94% 16%, var(--mist) 0, rgba(202,222,239,0) 30%),
      linear-gradient(180deg, #f7fbfe 0%, var(--paper) 100%);
  }
  .brand {
    position: absolute; top: 52px; left: 0; width: 100%;
    display: flex; flex-direction: column; align-items: center; gap: 10px;
    z-index: 2;
  }
  .brand-mark {
    width: 58px; height: 58px; border-radius: 50%;
    background: var(--blue);
  }
  .brand-name {
    font-size: 38px; font-weight: 700; color: var(--navy);
    letter-spacing: -0.5px;
  }
  .headline {
    position: absolute; top: 205px; left: 0; width: 100%;
    text-align: center; line-height: 1.08;
    z-index: 2;
  }
  .headline-lead {
    display: block; color: var(--blue);
    font-size: 58px; font-weight: 800; letter-spacing: -0.5px;
    white-space: nowrap;
  }
  .headline-strong {
    display: block; color: var(--ink);
    font-size: 60px; font-weight: 900; margin-top: 4px; letter-spacing: -0.5px;
    white-space: nowrap;
  }
  .staff-photo {
    position: absolute; top: 430px; left: 0; width: 1000px; height: 520px;
    background: linear-gradient(180deg, #ffffff 0%, var(--ice) 18%, #c9d8e6 60%, #8fa8c0 100%);
  }
  .respect-banner {
    position: absolute; top: 895px; left: 150px; width: 700px; height: 96px;
    background: var(--blue); border-radius: 14px;
    display: flex; align-items: center; justify-content: center;
    text-align: center; color: var(--paper);
    font-size: 26px; font-weight: 700; line-height: 1.25; padding: 0 40px;
    z-index: 2;
  }
  .behaviour-band {
    position: absolute; top: 950px; left: 0; width: 1000px; height: 190px;
    background: var(--band); color: var(--paper);
    padding: 62px 48px 0;
  }
  .behaviour-title {
    font-size: 23px; font-weight: 500; letter-spacing: 0.3px; white-space: nowrap;
  }
  .behaviour-title strong { font-weight: 700; }
  .behaviour-list {
    list-style: none; display: grid;
    grid-template-columns: repeat(6, 1fr); gap: 14px;
    margin-top: 22px;
  }
  .behaviour-item {
    display: flex; gap: 8px; align-items: flex-start;
    font-size: 13px; line-height: 1.3; color: #dfe4ea;
  }
  .behaviour-item svg { flex: 0 0 22px; }
  .policy-notes {
    position: absolute; top: 1180px; left: 48px; width: 904px;
    display: grid; grid-template-columns: repeat(3, 1fr); gap: 44px;
    font-size: 15px; line-height: 1.5; color: var(--muted);
  }
</style>
</head>
<body>
  <main class="flyer">
    <div class="network-backdrop" role="img" aria-label="Soft light-blue molecular network pattern"></div>

    <div class="staff-photo" role="img" aria-label="Photo of smiling clinic staff — doctors and nurses in white coats and blue scrubs — standing together as a team"></div>

    <header class="brand">
      <span class="brand-mark"></span>
      <span class="brand-name">Riverside Urology</span>
    </header>

    <h1 class="headline">
      <span class="headline-lead">WE HAVE ZERO-TOLERANCE</span>
      <span class="headline-lead">FOR ANY FORM OF</span>
      <span class="headline-strong">AGGRESSIVE BEHAVIOUR</span>
    </h1>

    <p class="respect-banner">Our staff treat you with respect and we expect the same in return</p>

    <section class="behaviour-band">
      <h2 class="behaviour-title"><strong>AGGRESSIVE BEHAVIOUR</strong> (IN-PERSON OR ON THE TELEPHONE) IS:</h2>
      <ul class="behaviour-list">
        <li class="behaviour-item"><svg width="22" height="22" viewBox="0 0 22 22"><circle cx="11" cy="11" r="9.5" fill="none" stroke="#6FCCEA" stroke-width="1.6"/><path d="M6.5 11.3l3 3 6-6.3" fill="none" stroke="#6FCCEA" stroke-width="1.8"/></svg>Verbal or written abuse</li>
        <li class="behaviour-item"><svg width="22" height="22" viewBox="0 0 22 22"><circle cx="11" cy="11" r="9.5" fill="none" stroke="#6FCCEA" stroke-width="1.6"/><path d="M6.5 11.3l3 3 6-6.3" fill="none" stroke="#6FCCEA" stroke-width="1.8"/></svg>Any verbal or physical intimidation</li>
        <li class="behaviour-item"><svg width="22" height="22" viewBox="0 0 22 22"><circle cx="11" cy="11" r="9.5" fill="none" stroke="#6FCCEA" stroke-width="1.6"/><path d="M6.5 11.3l3 3 6-6.3" fill="none" stroke="#6FCCEA" stroke-width="1.8"/></svg>Raising your voice or making unreasonable demands</li>
        <li class="behaviour-item"><svg width="22" height="22" viewBox="0 0 22 22"><circle cx="11" cy="11" r="9.5" fill="none" stroke="#6FCCEA" stroke-width="1.6"/><path d="M6.5 11.3l3 3 6-6.3" fill="none" stroke="#6FCCEA" stroke-width="1.8"/></svg>Abusive or threatening behaviour</li>
        <li class="behaviour-item"><svg width="22" height="22" viewBox="0 0 22 22"><circle cx="11" cy="11" r="9.5" fill="none" stroke="#6FCCEA" stroke-width="1.6"/><path d="M6.5 11.3l3 3 6-6.3" fill="none" stroke="#6FCCEA" stroke-width="1.8"/></svg>Use of foul language or gestures</li>
        <li class="behaviour-item"><svg width="22" height="22" viewBox="0 0 22 22"><circle cx="11" cy="11" r="9.5" fill="none" stroke="#6FCCEA" stroke-width="1.6"/><path d="M6.5 11.3l3 3 6-6.3" fill="none" stroke="#6FCCEA" stroke-width="1.8"/></svg>Making threats to our staff</li>
      </ul>
    </section>

    <section class="policy-notes">
      <p>If any of our staff feel intimidated in any way, we will always support them. Incidents will result in your immediate removal from the practice and may lead to prosecution.</p>
      <p>In all circumstances we will support any staff member who wishes to press charges against a perpetrator of aggressive behaviour.</p>
      <p>We take this stance because our staff work extremely hard to treat you well, and no one should face aggression or abuse at work.</p>
    </section>
  </main>
</body>
</html>
```